Website redesign for Halt and reBloom

We would like to update the design of our current website to a more concise, conversion optimized design.
The goal of our website is to get our message across as concisely as possible plus encourage people to contact us for more information or to book a consultation.
We need a redesign of the home page and 1 internal page - just for design/layout purposes/format purposes.

Target Market(s)

Males 20-45 years old who are concerned about hair loss and who want to regrow their own hair.

Industry/Entity Type

Health And Wellness

Number of Pages Required

2 page

Font styles to use
Sans Serif

Colors
00a990
33a6d7
ffffff
9d9d9d

Requirements
Must have
• We want the home page to be very concise and to the point in getting the message across. We want to get across the following 6 key messages:
• 1. Dr Quimby story – why he created this solution
• 2. Hair loss is caused by a chemical imbalance
• 3. Halt and rebloom conducts genetic and DNA analysis, then rebalances body chemistry, thus reversing the hair loss process and enabling your own hair to regrow naturally
• 4. Money back guaranteed results
• 5. Only The Active ingredients – no harsh preservatives or chemicals are included
• 6. All ingredients are FDA approved and safe – no side effects
• We also need a strong call to action. We want people to call or email us to find out more information or to schedule a consultation.
• Here is our current website which is not performing as we would hope: http://www.haltandrebloom-example.com/
• Here is our press release for further information: https://www.pressdeskly-example.com/news/finally-we-now-have-a-cure-for-male-pattern-baldness-19187647
• I uploaded the logo files, but let me know if anything else is needed and I can add it.

```html
<!DOCTYPE html>
<html lang="en">
<head>
<meta charset="utf-8">
<title>Halt and reBloom – Home</title>
<link rel="stylesheet" href="https://fonts.googleapis.com/css2?family=Open+Sans:wght@400;600&family=Oswald:wght@400;500&display=swap">
<style>
:root{
  --teal:#00a990;
  --sky:#33a6d7;
  --white:#ffffff;
  --grey:#9d9d9d;
  --ink:#333333;
  --text:#555555;
  --panel:#f3f3f3;
  --benefit:#3a7ad6;
  --hero-a:#2b2f33;
  --hero-b:#55585a;
}
*{margin:0;padding:0;box-sizing:border-box}
html,body{width:1200px;height:2723px;overflow:hidden;background:var(--white)}
body{position:relative;font-family:"Open Sans",Arial,sans-serif;color:var(--ink)}
.abs{position:absolute}

/* header */
.site-header{position:absolute;left:0;top:0;width:1200px;height:131px;background:var(--white)}
.header-phone{left:95px;top:40px;display:flex;align-items:center;gap:8px;font-size:22px;color:var(--ink)}
.brand{left:0;width:1200px;top:38px;text-align:center;font-size:24px;color:#6d6f71;font-weight:400;letter-spacing:3px}
.social-top{right:98px;top:41px;display:flex;gap:11px}
.social-top span{width:22px;height:22px;border-radius:3px;background:var(--sky)}
.social-top span:last-child{background:#d9352b}

.main-nav{left:87px;top:110px;width:1024px;height:53px;background:var(--teal);border-radius:3px;display:flex;align-items:center;padding-left:28px;gap:34px;z-index:2;box-shadow:0 2px 4px rgba(0,0,0,.2)}
.main-nav a{color:var(--white);text-decoration:none;font-size:15.5px;text-transform:uppercase}

/* hero */
.hero{left:0;top:131px;width:1200px;height:526px;background:linear-gradient(100deg,var(--hero-a),var(--hero-b) 45%,#3a3d40)}
.hero-title{left:0;width:1200px;top:390px;text-align:center;font-family:"Oswald",Arial,sans-serif;font-size:46px;color:var(--white);font-weight:400}
.hero-sub{left:0;width:1200px;top:448px;text-align:center;font-family:"Oswald",Arial,sans-serif;font-size:27px;color:var(--white)}
.hero-arrows{left:96px;top:582px;display:flex;gap:8px}
.hero-arrows span{width:26px;height:26px;border-radius:50%;background:rgba(0,0,0,.45);display:flex;align-items:center;justify-content:center}

/* welcome */
.welcome-title{left:91px;top:742px;font-size:28px;font-weight:400;color:var(--ink);white-space:nowrap}
.welcome-sub{left:91px;top:789px;font-size:15px;color:var(--ink);white-space:nowrap}
.welcome-copy{left:91px;top:818px;width:482px;font-size:12.4px;line-height:23px;color:#7a7a7a;text-align:justify}
.btn-outline{left:91px;top:974px;width:112px;height:36px;border:1.5px solid var(--teal);border-radius:18px;color:var(--teal);font-size:12.5px;display:flex;align-items:center;justify-content:center}
.video-frame{left:608px;top:728px;width:505px;height:289px;border:1px solid #d8d8d8;padding:4px;background:var(--white);box-shadow:0 1px 4px rgba(0,0,0,.15)}
.video-frame .media{width:100%;height:100%;background:linear-gradient(120deg,#8a6f5c,#c9a78f 50%,#6e5a4e)}
.play{left:831px;top:845px;width:56px;height:56px;border-radius:50%;background:rgba(40,40,40,.75)}

/* services */
.services{left:0;top:1080px;width:1200px;height:535px;background:var(--panel)}
.section-title{left:0;width:1200px;text-align:center;font-size:29px;font-weight:400;color:var(--ink)}
.service{width:300px;text-align:center}
.service .disc{width:180px;height:180px;margin:0 auto;border-radius:50%;border:4px solid var(--white);box-shadow:0 0 0 1px #cfcfcf}
.service h3{margin-top:24px;font-size:16.5px;font-weight:400;text-transform:uppercase;color:var(--ink);white-space:nowrap}
.service p{margin:8px auto 0;width:275px;height:66px;overflow:hidden;font-size:13px;line-height:22px;color:#7d7d7d}
.service a{display:block;margin-top:6px;font-size:14px;color:var(--sky);text-decoration:none}

/* benefits */
.benefits{left:0;top:1615px;width:1200px;height:414px;background:var(--benefit)}
.benefit-photo{left:134px;top:1686px;width:266px;height:266px;border-radius:50%;border:4px solid var(--white);background:linear-gradient(135deg,#c98f6e,#e8c2a4 55%,#8a5a40)}
.benefits-title{left:437px;top:1697px;font-size:30px;font-weight:400;color:var(--white)}
.benefit-list{left:437px;top:1750px;width:650px;list-style:none;color:var(--white);font-size:15.5px;line-height:24px}
.benefit-list li{position:relative;padding-left:20px;margin-bottom:5px}
.benefit-list li::before{content:"»";position:absolute;left:0;top:-1px}

/* blog */
.post{width:500px;height:145px}
.post .thumb{position:absolute;left:0;top:0;width:161px;height:144px}
.post .body{position:absolute;left:178px;top:4px;width:300px}
.post h4{font-size:15.5px;font-weight:400;color:var(--ink);white-space:nowrap}
.post time{display:block;margin-top:7px;font-size:12px;color:var(--ink)}
.post p{margin-top:5px;font-size:10.5px;line-height:21px;color:#555;white-space:nowrap}
.post a{display:block;margin-top:6px;font-size:12px;color:var(--teal);text-decoration:none}

/* footer */
.site-footer{left:0;top:2432px;width:1200px;height:291px;background:var(--panel)}
.foot-col{top:2487px}
.foot-col h5{font-size:15px;font-weight:400;text-transform:uppercase;color:var(--ink);margin-bottom:20px;white-space:nowrap}
.foot-col p{font-size:11.5px;line-height:22px;color:#666}
.signup{display:flex;margin-top:12px}
.signup span{width:148px;height:30px;border:1px solid #ccc;background:var(--white);font-size:11.5px;color:#777;padding:6px 8px}
.signup b{width:56px;height:30px;background:var(--teal);color:var(--white);font-weight:400;font-size:12px;display:flex;align-items:center;justify-content:center}
.social-foot{display:flex;gap:14px}
.social-foot span{width:24px;height:24px;border-radius:3px;background:#555}
.foot-rule{left:91px;top:2650px;width:1025px;height:1px;background:#cfcfcf}
.copyright{left:0;width:1200px;top:2679px;text-align:center;font-size:12.5px;color:var(--ink)}
</style>
</head>
<body>

<header class="site-header">
  <div class="abs header-phone">
    <svg width="20" height="20" viewBox="0 0 20 20" aria-hidden="true"><rect width="20" height="20" rx="3" fill="#33a6d7"/><path d="M6 4.5l2 .3.8 3-1.4 1a7 7 0 0 0 3.8 3.8l1-1.4 3 .8.3 2c-.2.9-1 1.5-1.9 1.5A10 10 0 0 1 4.5 6.4C4.5 5.5 5.1 4.7 6 4.5z" fill="#fff"/></svg>
    <span>(555) 014-2290</span>
  </div>
  <div class="abs brand">HALT AND REBLOOM</div>
  <div class="abs social-top" aria-label="Social links"><span></span><span></span><span></span><span></span></div>
</header>

<nav class="abs main-nav">
  <a href="#" aria-label="Home"><svg width="16" height="15" viewBox="0 0 16 15"><path d="M8 0L0 7h2v8h4V10h4v5h4V7h2z" fill="#fff"/></svg></a>
  <a href="#">About Us</a><a href="#">How It Works</a><a href="#">Success Stories</a><a href="#">FAQs</a><a href="#">Blog</a><a href="#">Salon Partners</a><a href="#">Book Now</a><a href="#">Contact</a>
</nav>

<section class="abs hero" role="img" aria-label="Doctor presenting to a seated audience in a hair salon"></section>
<h1 class="abs hero-title">HALT AND REBLOOM HAIR</h1>
<p class="abs hero-sub">Hair loss is caused by a chemical imbalance</p>
<div class="abs hero-arrows">
  <span><svg width="10" height="12" viewBox="0 0 10 12"><path d="M7 1L2 6l5 5" stroke="#fff" stroke-width="2" fill="none"/></svg></span>
  <span><svg width="10" height="12" viewBox="0 0 10 12"><path d="M3 1l5 5-5 5" stroke="#fff" stroke-width="2" fill="none"/></svg></span>
</div>

<h2 class="abs welcome-title">WELCOME TO HALT AND REBLOOM</h2>
<p class="abs welcome-sub">Halt Hereditary Hair Loss And Regrow a Full,&nbsp; Healthy Head of Hair</p>
<p class="abs welcome-copy">Dr. Alden Quimby, the creator of Halt and reBloom is a renowned hair restoration expert. After seeing first his father and then older brothers thin and go bald, he dedicated his life to finding the cure for hair loss. After initially pioneering the single hair method for hair transplant, he determined there must be a non-surgical solution and spent the last 20 years in research and clinical trial and error first creating, then perfecting what is now the Halt and reBloom</p>
<a class="abs btn-outline">Read More »</a>
<div class="abs video-frame"><div class="media" role="img" aria-label="Video still of a man checking his hairline"></div></div>
<div class="abs play"><svg width="56" height="56" viewBox="0 0 56 56"><path d="M22 17l17 11-17 11z" fill="#fff"/></svg></div>

<section class="abs services"></section>
<h2 class="abs section-title" style="top:1138px">OUR SERVICES</h2>
<div class="abs service" style="left:100px;top:1217px">
  <div class="disc" role="img" aria-label="Stylist examining a client's hair" style="background:linear-gradient(135deg,#6d8a86,#c8b8a6)"></div>
  <h3>Why is Halt and reBloom unique?</h3>
  <p>Halt and reBloom uses a scientific approach to hair loss by treating your unique cause. Every case is different and may include</p>
  <a href="#">How It Works -&gt;</a>
</div>
<div class="abs service" style="left:451px;top:1217px">
  <div class="disc" role="img" aria-label="Man running a hand through his hair" style="background:linear-gradient(135deg,#5a4a42,#c9a58d)"></div>
  <h3>Personalized Medicine</h3>
  <p>Halt and reBloom uses FDA approved ingredients in a proprietary formula using individual dosages based on your personal</p>
  <a href="#">See Success Stories -&gt;</a>
</div>
<div class="abs service" style="left:796px;top:1217px">
  <div class="disc" role="img" aria-label="Young man with a full head of hair" style="background:linear-gradient(135deg,#2e2e2e,#b99a80)"></div>
  <h3>Holistic Approach</h3>
  <p>While many cases of hair loss are caused by a hormone imbalance (DHT), stress and diet can cause hair loss too.&nbsp; Your treatment</p>
  <a href="#">Will It Work For You?</a>
</div>

<section class="abs benefits"></section>
<div class="abs benefit-photo" role="img" aria-label="Smiling couple"></div>
<h2 class="abs benefits-title">BENEFITS</h2>
<ul class="abs benefit-list">
  <li>Dr Quimby story – why he created this solution</li>
  <li>Hair loss is caused by a chemical imbalance</li>
  <li>Halt and rebloom conducts genetic and DNA analysis, then rebalances body chemistry, thus reversing the hair loss process and enabling your own hair to regrow naturally</li>
  <li>Money back guaranteed results</li>
  <li>Only The Active ingredients – no harsh preservatives or chemicals are included</li>
  <li>All ingredients are FDA approved and safe – no side effects</li>
</ul>

<h2 class="abs section-title" style="top:2118px">LATEST BLOG</h2>
<article class="abs post" style="left:91px;top:2203px">
  <div class="thumb" role="img" aria-label="Smiling man with short hair" style="background:linear-gradient(135deg,#e6e6e6,#b98d72)"></div>
  <div class="body">
    <h4>Neque porro quisquam est qui</h4>
    <time>09-07-2017</time>
    <p>Lorem Ipsum has been the industry's standard dummy<br>text ever since the 1500s, when an unknown printer took<br>a galley of type and scrambled it to make a type specimen</p>
    <a href="#">Read More &gt;&gt;</a>
  </div>
</article>
<article class="abs post" style="left:632px;top:2203px">
  <div class="thumb" role="img" aria-label="Man with long hair" style="background:linear-gradient(135deg,#3a2a22,#8a6a55)"></div>
  <div class="body">
    <h4>Neque porro quisquam est qui</h4>
    <time>09-07-2017</time>
    <p>Lorem Ipsum has been the industry's standard dummy<br>text ever since the 1500s, when an unknown printer took<br>a galley of type and scrambled it to make a type specimen</p>
    <a href="#">Read More &gt;&gt;</a>
  </div>
</article>

<footer class="abs site-footer"></footer>
<div class="abs foot-col" style="left:89px">
  <h5>Hours of Operation</h5>
  <p>Monday - Friday: 9.00am to 5.00pm<br>Saturday: 8.00am to 2.00pm</p>
</div>
<div class="abs foot-col" style="left:358px">
  <h5>Contact Us</h5>
  <p>Address : 1180 Larkspur Ave, Suite 300<br>Cedar Vale CA 90000&nbsp; United States<br>Phone : (555) 014-2290<br>Email : info@samplemail-example.com</p>
</div>
<div class="abs foot-col" style="left:648px;width:230px">
  <h5>Join Our Mailing List</h5>
  <p>Your about us information would fit<br>here nicely.</p>
  <div class="signup"><span>Email address</span><b>Submit</b></div>
</div>
<div class="abs foot-col" style="left:938px">
  <h5>Follow Us Out There</h5>
  <div class="social-foot" aria-label="Social links"><span></span><span></span><span></span><span></span></div>
</div>
<div class="abs foot-rule"></div>
<p class="abs copyright">Copyright © 2017. All Rights Reserved</p>

</body>
</html>
```